SipNOW Business Cards

Hi designers!

Here's some background on our start-up and this project:

SipNOW is a website that will allow users to order alcohol from nearby liquor stores and have it delivered to their homes in minutes. We are really excited to work on creating the best online, alcohol purchasing experience for the users.

So why SipNOW? We like to think of ourselves as that great friend who will get alcohol for you because he happens to have a car. We help you drink in with your friends, family, or guests. Our site will target students and young professionals (of drinking age) who are comfortable buying things online or through apps. We don't see this service as a luxury, VIP, or niche service in the least; instead, we think of us as a relaxed, service-driven start-up that believes in simple design and transparent .

Now, we want a business card that incorporates our newly acquired logo design and some complimenting colors and fonts. Feel free to do it single or double sided, although I'm a sucker for double...

If you happen to have any questions, want to throw some ideas around, or just want some feedback- email me at marco@sipnow.example.

Marco Tessin
Founder

Industry/Entity Type

Business

Requirements
Must have
• Name, Position, Email, Cell-phone

No address, no fax, no land-line.

```html
<!DOCTYPE html>
<html lang="en">
<head>
<meta charset="UTF-8">
<title>SipNOW Business Card</title>
<link rel="stylesheet" href="https://fonts.googleapis.com/css2?family=Mulish:wght@800&family=Questrial&display=swap">
<style>
  :root {
    --sun: #f8c418;
    --sun-soft: #fad75a;
    --ink: #231f20;
    --paper: #ffffff;
    --stage: #f2f2f2;
  }
  * { margin: 0; padding: 0; box-sizing: border-box; }
  html, body {
    width: 1200px;
    height: 1000px;
    overflow: hidden;
    background: var(--stage);
  }
  .canvas {
    position: relative;
    width: 1200px;
    height: 1000px;
  }
  .card {
    position: absolute;
    left: 220px;
    width: 760px;
    height: 420px;
    overflow: hidden;
  }
  .card--front { top: 70px; background: var(--paper); }
  .card--back { top: 520px; background: var(--sun); }

  .brand {
    position: absolute;
    left: 0;
    top: 0;
    width: 100%;
    height: 178px;
    display: flex;
    align-items: center;
    justify-content: center;
    gap: 22px;
  }
  .brand__square {
    width: 56px;
    height: 56px;
    background: var(--sun);
  }
  .brand__name {
    font-family: "Questrial", sans-serif;
    font-size: 76px;
    line-height: 1;
    letter-spacing: 4px;
    color: var(--ink);
  }
  .tagline-band {
    position: absolute;
    left: 0;
    top: 178px;
    width: 100%;
    height: 44px;
    background: var(--sun);
    display: flex;
    align-items: center;
    justify-content: center;
  }
  .tagline {
    font-family: "Mulish", sans-serif;
    font-weight: 800;
    font-size: 20px;
    letter-spacing: 6px;
    color: var(--paper);
    text-transform: uppercase;
  }
  .holder {
    position: absolute;
    top: 252px;
    width: 100%;
    text-align: center;
    font-family: "Questrial", sans-serif;
    color: var(--ink);
  }
  .holder__name {
    font-size: 24px;
    letter-spacing: 4px;
    -webkit-text-stroke: 0.6px var(--ink);
  }
  .holder__role {
    margin-top: 6px;
    font-size: 14px;
    letter-spacing: 4px;
    text-transform: uppercase;
  }
  .contact {
    position: absolute;
    top: 340px;
    width: 100%;
    display: flex;
    justify-content: center;
    align-items: center;
    gap: 18px;
    font-family: "Questrial", sans-serif;
    font-size: 20px;
    letter-spacing: 1.5px;
    color: var(--ink);
  }
  .contact__divider {
    width: 2px;
    height: 24px;
    background: var(--sun);
  }

  .back-brand {
    position: absolute;
    inset: 0;
    display: flex;
    align-items: center;
    justify-content: center;
    font-family: "Questrial", sans-serif;
    font-size: 76px;
    letter-spacing: 4px;
    color: var(--sun-soft);
  }
</style>
</head>
<body>
<main class="canvas">
  <section class="card card--front" aria-label="Business card front">
    <div class="brand">
      <span class="brand__square"></span>
      <span class="brand__name">SipNOW</span>
    </div>
    <div class="tagline-band"><p class="tagline">We bring the drinks to you!</p></div>
    <div class="holder">
      <p class="holder__name">Marco Tessin</p>
      <p class="holder__role">Founder</p>
    </div>
    <div class="contact">
      <span>marco@sipnow.example</span>
      <span class="contact__divider"></span>
      <span>123.456.7890</span>
      <span class="contact__divider"></span>
      <span>urlgoeshere.com</span>
    </div>
  </section>

  <section class="card card--back" aria-label="Business card back">
    <p class="back-brand">SipNOW</p>
  </section>
</main>
</body>
</html>
```